Plate Bright Workshop (workshop to teach people to eat fruits and vegetables)

Double sided DL Flyer

Free Community Workshop
Plate Bright Live Lively
Central Coast NSW

Copy to appear on flyer side one:-
PLATE BRIGHT LIVE LIVELY
interactive workshops
March-April 2019
Presented by qualified nutritionist

Food for healthier happier life for you and your family (free to central coast residents - all ages welcome

Side 2
Learn About:-
Foods that improve your health
basic nutrition
gut brain connection
portion size
menu planning
preparation
eating

Benefits
Improved health
Improved Energy
Manage chronic illness
diabetes type II
cholesterol
Blood Pressure
Family fun

Food Tastings
Lucky Door Prize

Reserve for spot online @ www.platebright.com.au or call 0462 508 731
Supported by Harbourline Shire Council (Logo) Harbourline Rugby Social Club (Logo) Pindara Veterans Club (Logo)

I would like to see a flyer that is bright, fun and fresh with images of fresh food.

Target Market(s)

Women 30 plus

Industry/Entity Type

Health And Wellness

Logo Text

PLATE BRIGHT LIVE LIVELY

Font styles to use
Other font styles liked:
• bold clean

Colors
f37122
9bcb3c
fbed22
ec1f27
e34297

Requirements
Must have
• bright eye catching colours featuring fresh fruit and vegetables
• I have attached a some images of designs I like
Nice to have
• Im happy for the designer to change copy to create a clean flyer without loosing essential information
• I like the feel of the banner on my facebook page
• Kindly Nourish - Plate Bright Live Lively with Megan Troute
• https://www.facebook.com/kindlynourishoz/
Should not have
• old fashioned images

```html
<!DOCTYPE html>
<html lang="en">
<head>
<meta charset="utf-8">
<title>Plate Bright Live Lively – DL Flyer</title>
<link rel="stylesheet" href="https://fonts.googleapis.com/css2?family=Source+Sans+3:wght@300;400;600;700;900&display=swap">
<style>
  :root {
    --stage: #9d9fa2;
    --sky: #d9eaf9;
    --purple: #6b2a8e;
    --plum: #8b2e91;
    --plum-light: #a63ca0;
    --magenta: #e5247f;
    --ink: #111111;
    --white: #ffffff;
  }
  * { box-sizing: border-box; margin: 0; padding: 0; }
  html, body { width: 1200px; height: 1200px; overflow: hidden; }
  body {
    background: var(--stage);
    font-family: "Source Sans 3", "Source Sans Pro", sans-serif;
    position: relative;
  }
  .flyer-side {
    position: absolute;
    top: 86px;
    width: 464px;
    height: 1028px;
    overflow: hidden;
  }
  .side-front {
    left: 126px;
    background: linear-gradient(180deg, var(--sky) 0%, #d3e6f8 50%, var(--sky) 100%);
    color: var(--ink);
    text-align: center;
  }
  .side-back {
    left: 610px;
    background: linear-gradient(160deg, var(--plum) 0%, var(--plum-light) 60%, var(--plum) 100%);
    color: var(--white);
  }
  .abs { position: absolute; left: 0; right: 0; }

  /* Front */
  .brand-name {
    top: 30px;
    left: 40px;
    right: 28px;
    font-weight: 900;
    font-size: 54px;
    line-height: 58px;
    color: var(--purple);
    letter-spacing: 1px;
  }
  .hero-art { position: absolute; left: 0; top: 232px; }
  .headline-thin {
    top: 632px;
    font-weight: 300;
    font-size: 67px;
    line-height: 67px;
    color: var(--purple);
  }
  .headline-bold {
    top: 692px;
    font-weight: 900;
    font-size: 42px;
    line-height: 42px;
    color: var(--purple);
  }
  .date-row {
    position: absolute;
    top: 742px;
    left: 114px;
    display: flex;
    gap: 9px;
    height: 52px;
  }
  .date-months {
    border: 2px solid var(--purple);
    width: 100px;
    color: var(--purple);
    font-weight: 900;
    font-size: 19px;
    line-height: 21px;
    padding-top: 4px;
  }
  .date-year {
    background: var(--purple);
    color: var(--white);
    width: 130px;
    font-weight: 700;
    font-size: 58px;
    line-height: 52px;
  }
  .presenter { top: 808px; font-size: 14px; line-height: 16px; font-weight: 400; }
  .tagline { top: 832px; font-size: 30px; line-height: 29px; font-weight: 600; }
  .tagline .lead { font-size: 27px; display: block; }
  .tagline strong { font-weight: 900; display: block; }
  .access { top: 944px; font-size: 17.5px; line-height: 20px; font-weight: 300; }
  .welcome { top: 966px; font-size: 26px; line-height: 30px; font-weight: 600; }

  /* Back */
  .back-photo { position: absolute; left: 0; top: 0; }
  .copy-block { position: absolute; top: 324px; left: 21px; right: 6px; }
  .section-title { font-size: 28px; font-weight: 600; line-height: 30px; }
  .check-list { list-style: none; margin: 2px 0 10px 0; }
  .check-list li {
    font-size: 24px;
    line-height: 28.8px;
    padding-left: 75px;
    position: relative;
    font-weight: 400;
  }
  .check-list li .tick { position: absolute; left: 40px; top: 5px; }
  .check-list li.sub { padding-left: 101px; }
  .check-list li.sub .arrow { position: absolute; left: 81px; top: 8px; }
  .booking { position: absolute; top: 834px; left: 0; right: 16px; text-align: center; }
  .booking-lead { font-size: 21px; line-height: 24px; font-weight: 400; }
  .booking-url { font-size: 29.5px; line-height: 28px; font-weight: 400; }
  .booking-or { font-size: 26px; line-height: 26px; }
  .booking-phone { font-size: 31px; line-height: 30px; font-weight: 700; display: inline-flex; align-items: center; gap: 4px; }
  .supporters-label { position: absolute; top: 933px; left: 21px; font-size: 16px; line-height: 18px; font-weight: 300; }
  .supporter {
    position: absolute;
    top: 955px;
    width: 110px;
    text-align: center;
    font-size: 10px;
    line-height: 11px;
    font-weight: 400;
  }
  .supporter .mark {
    width: 40px; height: 40px; border-radius: 50%;
    background: var(--white);
    margin: 0 auto 3px;
  }
  .supporter.wide .mark { width: 72px; height: 36px; margin-top: 4px; }
  .supporter.square .mark { border-radius: 2px; }
</style>
</head>
<body>

<section class="flyer-side side-front">
  <div class="abs brand-name">PLATE<br>BRIGHT<br>LIVE LIVELY</div>

  <svg class="hero-art" width="464" height="390" viewBox="0 0 464 390">
    <path d="M80 60 C140 0 250 -10 330 40 C420 95 470 160 440 250 C410 330 320 380 200 378 C110 376 70 330 60 260 C50 180 30 110 80 60 Z" fill="var(--purple)"/>
    <path d="M100 90 C150 40 250 30 330 90 C400 140 430 200 410 260 C390 310 300 340 190 330 C120 325 80 280 78 220 C76 160 70 120 100 90 Z" fill="var(--magenta)"/>
    <defs>
      <linearGradient id="produceTones" x1="0" y1="0" x2="1" y2="1">
        <stop offset="0" stop-color="#e8564a"/>
        <stop offset="0.3" stop-color="#f2a532"/>
        <stop offset="0.55" stop-color="#7fb83e"/>
        <stop offset="0.75" stop-color="#8a4aa0"/>
        <stop offset="1" stop-color="#4f8d2c"/>
      </linearGradient>
    </defs>
    <path role="img" aria-label="Photo of fresh fruit and vegetables in a wooden crate: grapefruit, apples, grapes, purple kale, capsicum, radishes and lettuce"
      d="M0 120 C40 100 90 120 110 70 C150 20 250 10 330 60 C400 105 430 170 420 240 C410 300 340 345 230 345 C150 345 90 350 40 330 C10 320 0 300 0 280 Z"
      fill="url(#produceTones)"/>
  </svg>

  <div class="abs headline-thin">INTERACTIVE</div>
  <div class="abs headline-bold">WORKSHOPS</div>
  <div class="date-row">
    <div class="date-months">MARCH<br>&amp; APRIL</div>
    <div class="date-year">2019</div>
  </div>
  <div class="abs presenter">PRESENTED BY QUALIFIED NUTRITIONIST</div>
  <div class="abs tagline"><span class="lead">FOOD FOR A</span><strong>HEALTHIER HAPPIER LIFE</strong>FOR YOU AND YOUR FAMILY</div>
  <div class="abs access">FREE FOR NSW CENTRAL COAST RESIDENTS</div>
  <div class="abs welcome">ALL AGES WELCOME</div>
</section>

<section class="flyer-side side-back">
  <svg class="back-photo" width="464" height="312" viewBox="0 0 464 312">
    <defs>
      <linearGradient id="fruitTones" x1="0" y1="0" x2="1" y2="1">
        <stop offset="0" stop-color="#f3b23a"/>
        <stop offset="0.35" stop-color="#e94a4a"/>
        <stop offset="0.6" stop-color="#f08a3c"/>
        <stop offset="0.8" stop-color="#8bbf3f"/>
        <stop offset="1" stop-color="#d8304a"/>
      </linearGradient>
    </defs>
    <path d="M0 0 H464 V222 C400 280 300 312 200 308 C110 304 40 262 0 212 Z" fill="var(--white)"/>
    <path role="img" aria-label="Photo of a colourful fruit platter: grapefruit, oranges, limes, kiwi, mango, berries and pineapple"
      d="M0 0 H464 V212 C400 270 300 302 200 298 C110 294 40 252 0 202 Z" fill="url(#fruitTones)"/>
  </svg>

  <div class="copy-block">
    <div class="section-title">LEARN ABOUT:</div>
    <ul class="check-list">
      <li><svg class="tick" width="18" height="18" viewBox="0 0 18 18"><rect x="1" y="3" width="13" height="13" fill="none" stroke="#fff" stroke-width="2"/><path d="M4 9 L8 13 L17 1" fill="none" stroke="#fff" stroke-width="2.4"/></svg>FOODS THAT IMPROVE YOUR<br>HEALTH</li>
      <li><svg class="tick" width="18" height="18" viewBox="0 0 18 18"><rect x="1" y="3" width="13" height="13" fill="none" stroke="#fff" stroke-width="2"/><path d="M4 9 L8 13 L17 1" fill="none" stroke="#fff" stroke-width="2.4"/></svg>BASIC NUTRITION</li>
      <li><svg class="tick" width="18" height="18" viewBox="0 0 18 18"><rect x="1" y="3" width="13" height="13" fill="none" stroke="#fff" stroke-width="2"/><path d="M4 9 L8 13 L17 1" fill="none" stroke="#fff" stroke-width="2.4"/></svg>GUT BRAIN CONNECTION</li>
      <li><svg class="tick" width="18" height="18" viewBox="0 0 18 18"><rect x="1" y="3" width="13" height="13" fill="none" stroke="#fff" stroke-width="2"/><path d="M4 9 L8 13 L17 1" fill="none" stroke="#fff" stroke-width="2.4"/></svg>PORTION SIZE</li>
      <li><svg class="tick" width="18" height="18" viewBox="0 0 18 18"><rect x="1" y="3" width="13" height="13" fill="none" stroke="#fff" stroke-width="2"/><path d="M4 9 L8 13 L17 1" fill="none" stroke="#fff" stroke-width="2.4"/></svg>MENU PLANNING</li>
      <li><svg class="tick" width="18" height="18" viewBox="0 0 18 18"><rect x="1" y="3" width="13" height="13" fill="none" stroke="#fff" stroke-width="2"/><path d="M4 9 L8 13 L17 1" fill="none" stroke="#fff" stroke-width="2.4"/></svg>PREPARATION</li>
      <li><svg class="tick" width="18" height="18" viewBox="0 0 18 18"><rect x="1" y="3" width="13" height="13" fill="none" stroke="#fff" stroke-width="2"/><path d="M4 9 L8 13 L17 1" fill="none" stroke="#fff" stroke-width="2.4"/></svg>EATING</li>
    </ul>
    <div class="section-title">BENEFITS:</div>
    <ul class="check-list">
      <li><svg class="tick" width="18" height="18" viewBox="0 0 18 18"><rect x="1" y="3" width="13" height="13" fill="none" stroke="#fff" stroke-width="2"/><path d="M4 9 L8 13 L17 1" fill="none" stroke="#fff" stroke-width="2.4"/></svg>IMPROVED HEALTH</li>
      <li><svg class="tick" width="18" height="18" viewBox="0 0 18 18"><rect x="1" y="3" width="13" height="13" fill="none" stroke="#fff" stroke-width="2"/><path d="M4 9 L8 13 L17 1" fill="none" stroke="#fff" stroke-width="2.4"/></svg>IMPROVED ENERGY</li>
      <li><svg class="tick" width="18" height="18" viewBox="0 0 18 18"><rect x="1" y="3" width="13" height="13" fill="none" stroke="#fff" stroke-width="2"/><path d="M4 9 L8 13 L17 1" fill="none" stroke="#fff" stroke-width="2.4"/></svg>MANAGE CHRONIC ILLNESS</li>
      <li class="sub"><svg class="arrow" width="14" height="14" viewBox="0 0 14 14"><path d="M1 1 L13 7 L1 13 Z" fill="#fff"/></svg>DIABETES TYPE II</li>
      <li class="sub"><svg class="arrow" width="14" height="14" viewBox="0 0 14 14"><path d="M1 1 L13 7 L1 13 Z" fill="#fff"/></svg>CHOLESTEROL</li>
      <li class="sub"><svg class="arrow" width="14" height="14" viewBox="0 0 14 14"><path d="M1 1 L13 7 L1 13 Z" fill="#fff"/></svg>BLOOD PRESSURE</li>
      <li><svg class="tick" width="18" height="18" viewBox="0 0 18 18"><rect x="1" y="3" width="13" height="13" fill="none" stroke="#fff" stroke-width="2"/><path d="M4 9 L8 13 L17 1" fill="none" stroke="#fff" stroke-width="2.4"/></svg>FAMILY FUN</li>
    </ul>
  </div>

  <div class="booking">
    <div class="booking-lead">RESERVE YOUR SPOT ONLINE AT</div>
    <div class="booking-url">WWW.PLATEBRIGHT.COM.AU</div>
    <div class="booking-or">OR</div>
    <div class="booking-phone">
      <svg width="30" height="28" viewBox="0 0 30 28"><path d="M6 26 C2 22 2 14 8 7 C14 1 22 0 26 3 L22 9 C19 8 16 9 13 12 C10 15 9 18 10 21 L6 26 Z" fill="#fff"/></svg>
      0462 508 731
    </div>
  </div>

  <div class="supporters-label">Supported by</div>
  <div class="supporter wide" style="left:3px;"><div class="mark"></div>Harbourline Rugby<br>Social Club</div>
  <div class="supporter square" style="left:190px;"><div class="mark"></div>Pindara<br>Veterans Club</div>
  <div class="supporter" style="left:352px;"><div class="mark"></div>Harbourline<br>Shire Council</div>
</section>

</body>
</html>
```